Letterhead to coordinate with business card

I am needing a docx template and print file for a letterhead to co-ordinate with my newly designed logo and business card.

```html
<!DOCTYPE html>
<html lang="en">
<head>
<meta charset="utf-8">
<title>Harbor Plan Partners – Letterhead</title>
<link href="https://fonts.googleapis.com/css2?family=Outfit:wght@400;600&display=swap" rel="stylesheet">
<style>
  :root{
    --canvas:#e4e4e4;
    --paper:#ffffff;
    --ink:#26262b;
    --navy:#2f3440;
    --navy-deep:#262a33;
    --teal:#0e8580;
    --teal-bright:#00a99d;
    --purple:#6f2966;
    --magenta:#a8336a;
  }
  *{margin:0;padding:0;box-sizing:border-box}
  html,body{width:1200px;height:1200px;overflow:hidden;background:var(--canvas)}
  body{font-family:"Outfit",sans-serif;color:var(--ink)}
  .letterhead{
    position:absolute;left:234px;top:82px;width:732px;height:1036px;
    background:var(--paper);box-shadow:0 2px 10px rgba(0,0,0,.12);overflow:hidden;
  }
  .header-band{
    position:absolute;left:0;top:0;width:100%;height:72px;
    background:linear-gradient(90deg,var(--navy) 0%,var(--navy-deep) 100%);
  }
  .brand{position:absolute;left:58px;top:124px;display:flex;align-items:center;gap:10px}
  .brand-square{width:30px;height:30px;background:var(--teal)}
  .brand-name{font-weight:600;font-size:21px;color:var(--magenta)}
  .recipient{position:absolute;left:64px;top:280px;font-size:14px;line-height:19.7px;font-style:normal;letter-spacing:.2px}
  .salutation{position:absolute;left:64px;top:418px;font-size:14px;letter-spacing:.2px}
  .body-copy{position:absolute;left:64px;top:457px;width:594px;font-size:14px;line-height:19.7px;text-align:justify;letter-spacing:.2px}
  .signature{position:absolute;left:64px;top:786px;width:183px;height:47px;background:rgba(38,38,43,.08)}
  .contact{position:absolute;top:970px;font-size:9.6px;line-height:15px}
  .contact-left{left:60px}
  .contact-right{left:270px}
  .contact-item{display:flex;align-items:center;gap:5px}
  .contact-item svg{width:9px;height:9px;flex:none}
  .contact-item strong{font-weight:600;color:var(--purple)}
  .footer-bar{position:absolute;bottom:0;height:15px}
  .footer-bar-purple{left:0;width:366px;background:var(--purple)}
  .footer-bar-teal{left:369px;right:0;background:var(--teal-bright)}
</style>
</head>
<body>
<main class="letterhead">
  <div class="header-band" role="img" aria-label="Dark navy header band with teal and purple accent sweeps"></div>

  <div class="brand">
    <span class="brand-square"></span>
    <span class="brand-name">Harbor Plan Partners</span>
  </div>

  <address class="recipient">
    Mr. Sam Carter<br>
    President<br>
    Summit Advisory<br>
    27 Example Road,<br>
    Townsville State, 10000
  </address>

  <p class="salutation">Dear</p>

  <div class="body-copy">
    <p>Lorem ipsum dolor sit amet, consectetur adipiscing elit. Aenean ut ipsum eget massa hendrerit vestibulum vel in velit. Donec pretium neque velit.</p>
    <p>Aliquam porta lectus nec mauris ornare venenatis. Vivamus non est turpis, et cursus sem. Mauris vehicula erat in diam auctor at bibendum nisl lacinia.</p>
    <p>Morbi imperdiet neque vehicula nunc convallis gravida. Vestibulum iaculis pretium placerat. Integer consequat, est sit amet facilisis eleifend, nibh nibh varius orci, eget dapibus arcu dui non purus. Pellentesque in magna mauris. Duis enim sapien, dictum vitae condimentum a, pulvinar vel lacus. Mauris et molestie nibh. Vestibulum vitae nulla at metus elementum porta sit amet interdum elit. Nulla sollicitudin neque eu nulla volutpat congue.</p>
    <p>Etiam pellentesque, velit id dapibus fermentum, turpis sapien ornare dui, ac tincidunt ligula odio congue purus. Nunc sed ante dui, in porta lectus. Cras nec sem lorem. In hac habitasse platea dictumst. Maecenas id diam quis dui porta tristique. Sed id egestas felis. Donec ullamcorper mattis posuere. Phasellus fermentum eleifend tortor vel dapibus. Vestibulum ante ipsum.</p>
  </div>

  <div class="signature" role="img" aria-label="Handwritten signature of the sender"></div>

  <div class="contact contact-left">
    <div class="contact-item">
      <svg viewBox="0 0 10 10" aria-hidden="true"><path d="M2.2 1 3.6 2.6 2.9 3.6C3.5 4.9 4.9 6.4 6.3 7.1L7.3 6.4 9 7.8 8.1 9C4.6 8.7 1.3 5.4 1 1.9Z" fill="var(--teal-bright)"/></svg>
      <span>0400 217 358</span>
    </div>
    <div class="contact-item">
      <svg viewBox="0 0 10 10" aria-hidden="true"><rect x="1" y="2.5" width="8" height="6" rx=".8" fill="var(--teal-bright)"/><path d="M1.3 3 5 6 8.7 3" stroke="#fff" stroke-width=".9" fill="none"/></svg>
      <span>info@harborplanpartners.com.au</span>
    </div>
  </div>

  <div class="contact contact-right">
    <div class="contact-item">
      <svg viewBox="0 0 10 10" aria-hidden="true"><g fill="none" stroke="var(--teal-bright)" stroke-width=".9"><circle cx="5" cy="5" r="4"/><ellipse cx="5" cy="5" rx="1.8" ry="4"/><path d="M1 5H9M1.6 3H8.4M1.6 7H8.4"/></g></svg>
      <span>www.<strong>harborplanpartners</strong>.com</span>
    </div>
    <div class="contact-item">
      <svg viewBox="0 0 10 10" aria-hidden="true"><path d="M5 .8A3 3 0 0 0 2 3.8C2 6 5 9.4 5 9.4S8 6 8 3.8A3 3 0 0 0 5 .8Z" fill="var(--teal-bright)"/><circle cx="5" cy="3.8" r="1.1" fill="#fff"/></svg>
      <span>PO Box 42, Lakeside NSW 2290</span>
    </div>
  </div>

  <div class="footer-bar footer-bar-purple"></div>
  <div class="footer-bar footer-bar-teal"></div>
</main>
</body>
</html>
```